Feminine colorfull packaging for coconut skin care brand

We need a design that can be used on different types of packaging for beauty products likes creams, oils, etc.
The products that we will launch will be made with one key ingredient of coconut oil + other added ingredients depending on the type of product. The entire marketing will therefore be based on COCONUTS, palmtrees, sand, beach, bronzing on the beach, holiday feeling, nature, femininity, etc. = A Lifestyle brand with a tropical vibe.
Packaging can be a pot for creams, flaskes for lotions, smaller bottles for oils, etc. Mostly the standard packaging used for beauty products.
We would like to use the color pink ( this can be bright or pastel or any tone of pink) to address the feminine side of our product and a tone of blue-green ( pastel, bright or any tone of this color) to accentuate the use of coconut.
Third would be the color white (this can be added through an accent somewhere on the packaging or this can be the brand name that is written in white)
Lastely we would like the packaging to be light, fresh and playfull. Please feel free to use different colors or shapes ( we do not yet have a logo. This can then be designed followed on the packaging)
The design will be printed on plastic packaging. We are open to very creative designs. We are looking for packaging that catches the eye by its design and/or colors, that is different than others, that distinguishes the product because of its packaging design.
Target Market(s)
Women between 20 - 35 years
Industry/Entity Type
Beauty
Colors
Designer to choose colors to be used in the design.
Look and feel

```html
<!DOCTYPE html>
<html lang="en">
<head>
<meta charset="utf-8">
<title>Kaimana Body Lotion – Jar Label</title>
<link rel="stylesheet" href="https://fonts.googleapis.com/css2?family=Montserrat:wght@400;600&display=swap">
<style>
  :root {
    --page-bg: #f4f2ef;
    --lid-pink: #f6dfe2;
    --lid-shade: #ecc9ce;
    --label-teal: #86b9ab;
    --label-teal-deep: #79ad9f;
    --leaf-pink: #f1cfd5;
    --brand-white: #ffffff;
    --copy-blush: #f8e9eb;
  }
  * { margin: 0; padding: 0; box-sizing: border-box; }
  html, body {
    width: 1200px;
    height: 900px;
    overflow: hidden;
    background: var(--page-bg);
    font-family: "Montserrat", sans-serif;
  }
  .canvas {
    position: relative;
    width: 1200px;
    height: 900px;
    display: flex;
    flex-direction: column;
    align-items: center;
    justify-content: center;
  }
  .lid-band {
    width: 820px;
    height: 150px;
    border-radius: 28px 28px 10px 10px;
    background: linear-gradient(180deg, var(--lid-pink) 70%, var(--lid-shade));
  }
  .label-panel {
    position: relative;
    width: 800px;
    height: 420px;
    margin-top: 14px;
    border-radius: 10px 10px 40px 40px;
    background: linear-gradient(180deg, var(--label-teal), var(--label-teal-deep));
    overflow: hidden;
  }
  .palm-leaf {
    position: absolute;
    border-radius: 50% 50% 50% 50% / 70% 70% 30% 30%;
    background: linear-gradient(160deg, var(--leaf-pink), rgba(241, 207, 213, 0.35));
    opacity: 0.8;
  }
  .palm-leaf--top-left { left: -10px; top: 10px; width: 140px; height: 150px; transform: rotate(-30deg); }
  .palm-leaf--bottom-left { left: 60px; top: 230px; width: 150px; height: 190px; transform: rotate(-20deg); }
  .palm-leaf--right { right: 30px; top: 40px; width: 90px; height: 260px; transform: rotate(12deg); }
  .brand-name {
    position: absolute;
    top: 100px;
    left: 0;
    right: 0;
    text-align: center;
    color: var(--brand-white);
    font-weight: 600;
    font-size: 64px;
    letter-spacing: 8px;
  }
  .product-copy {
    position: absolute;
    top: 220px;
    left: 0;
    right: 0;
    text-align: center;
    color: var(--copy-blush);
    font-weight: 400;
    font-size: 34px;
    line-height: 1.15;
    letter-spacing: 1px;
  }
</style>
</head>
<body>
  <main class="canvas">
    <div class="lid-band"></div>
    <section class="label-panel">
      <div class="palm-leaf palm-leaf--top-left" role="img" aria-label="Pink palm leaf illustration"></div>
      <div class="palm-leaf palm-leaf--bottom-left" role="img" aria-label="Pink palm leaf illustration"></div>
      <div class="palm-leaf palm-leaf--right" role="img" aria-label="Pink palm leaf illustration"></div>
      <h1 class="brand-name">KAIMANA</h1>
      <p class="product-copy">body lotion<br>coconut extracts</p>
    </section>
  </main>
</body>
</html>
```